Business Card Design

We need a business card designed to the point of print ready to take to our printers. the design should be professional, easy to read and simple. The cards should represent our business as professional and trust worthy.

Attached are several versions o the logo, and also the details for the card to be printed. please do communicate if different versions of the logo is required.

Industry/Entity Type

Business

```html
<!DOCTYPE html>
<html lang="en">
<head>
<meta charset="utf-8">
<title>Ledgerwise Pty Ltd – Business Card</title>
<link rel="stylesheet" href="https://fonts.googleapis.com/css2?family=Open+Sans:wght@400;600;700;800&display=swap">
<style>
  :root {
    --backdrop: #ebe8e4;
    --card: #ffffff;
    --ink: #4a4a4a;
    --ink-dark: #2f2f2f;
    --ink-soft: #6b6b6b;
    --accent: #f5a01a;
    --rule: #b9b9b9;
  }
  * { box-sizing: border-box; margin: 0; padding: 0; }
  html, body {
    width: 1200px; height: 720px; overflow: hidden;
    background: var(--backdrop);
    font-family: "Open Sans", Arial, sans-serif;
    color: var(--ink);
  }
  .canvas {
    position: relative; width: 1200px; height: 720px;
    display: flex; align-items: center; justify-content: center; gap: 40px;
  }
  .card {
    position: relative; width: 540px; height: 330px;
    background: var(--card);
    box-shadow: 0 2px 10px rgba(0,0,0,.12);
    overflow: hidden;
  }
  .brand {
    position: absolute; display: flex; align-items: center; gap: 12px;
    font-weight: 700; color: var(--ink); letter-spacing: -0.5px; white-space: nowrap;
  }
  .brand-dot { width: 14px; height: 14px; border-radius: 50%; background: var(--accent); flex: none; }
  .brand-suffix { font-size: .42em; letter-spacing: 0; margin-left: 4px; }

  /* Front */
  .card-front .brand { top: 48px; left: 0; right: 0; justify-content: center; font-size: 46px; }
  .card-front .base-rule {
    position: absolute; left: 0; right: 0; top: 250px; height: 2px; background: var(--rule);
  }
  .address {
    position: absolute; top: 154px; right: 292px; text-align: right;
    font-size: 14px; line-height: 24px; color: var(--ink-soft);
  }
  .divider {
    position: absolute; top: 146px; left: 268px; width: 1px; height: 66px; background: var(--rule);
  }
  .contact-list {
    position: absolute; top: 140px; left: 284px; list-style: none;
    font-size: 14px; line-height: 25px; color: var(--ink-soft);
  }
  .contact-list li { display: flex; align-items: center; gap: 9px; }
  .contact-list svg { width: 15px; height: 15px; flex: none; }
  .name-band {
    position: absolute; left: 0; right: 0; top: 262px; height: 44px;
    background: var(--accent); color: #fff;
    display: flex; align-items: center; justify-content: center;
    font-size: 16px;
  }
  .name-band strong { font-weight: 700; margin-right: 6px; }

  /* Back */
  .card-back .brand { top: 110px; left: 0; right: 0; justify-content: center; font-size: 52px; }
  .web {
    position: absolute; bottom: 48px; left: 0; right: 0; text-align: center;
    font-size: 20px; letter-spacing: 1.5px; color: var(--ink);
  }
  .web b { font-weight: 700; color: var(--ink-dark); }
  .web .web-accent { color: var(--accent); }
</style>
</head>
<body>
<main class="canvas">
  <section class="card card-front" aria-label="Business card front">
    <div class="brand"><span class="brand-dot"></span>Ledgerwise<span class="brand-suffix">Pty Ltd</span></div>
    <address class="address">PO Box 2281 Q<br>Harbourside Qld 4220</address>
    <div class="divider"></div>
    <ul class="contact-list">
      <li>
        <svg viewBox="0 0 16 16" aria-hidden="true"><circle cx="8" cy="8" r="8" fill="var(--accent)"/><path d="M5.2 4.2l1.6-.4.9 2-1 .8a5 5 0 0 0 2.7 2.7l.8-1 2 .9-.4 1.6c-3.6.3-6.9-3-6.6-6.6z" fill="#fff"/></svg>
        +61 400 555 019
      </li>
      <li>
        <svg viewBox="0 0 16 16" aria-hidden="true"><circle cx="8" cy="8" r="8" fill="var(--accent)"/><rect x="4" y="5.2" width="8" height="5.6" fill="#fff"/><path d="M4 5.4l4 3 4-3" stroke="var(--accent)" stroke-width="1" fill="none"/></svg>
        hcorwell@ledgerwise.com.au
      </li>
      <li>
        <svg viewBox="0 0 16 16" aria-hidden="true"><circle cx="8" cy="8" r="8" fill="var(--accent)"/><circle cx="8" cy="8" r="4" fill="none" stroke="#fff" stroke-width="1.1"/><path d="M4 8h8M8 4c-2 2.4-2 5.6 0 8M8 4c2 2.4 2 5.6 0 8" stroke="#fff" stroke-width=".9" fill="none"/></svg>
        www.ledgerwise.com.au
      </li>
    </ul>
    <div class="base-rule"></div>
    <div class="name-band"><strong>Hannah Corwell,</strong> Managing Director</div>
  </section>

  <section class="card card-back" aria-label="Business card back">
    <div class="brand"><span class="brand-dot"></span>Ledgerwise<span class="brand-suffix">Pty Ltd</span></div>
    <p class="web">www.<b>ledger<span class="web-accent">wise</span></b>.com.au</p>
  </section>
</main>
</body>
</html>
```